Velmora Biz Card 2019

New business card for Velmora Property Inspections. We are a residential home inspection company in Arizona.

Target Market(s)

Real Estate

Font styles to use
Sans Serif

Requirements
Must have
• Glen Mirewick
• Home Inspector
• Velmora Property Inspections, LLC
• 480-555-0172
• glen@velmora-llc.example

```html
<!DOCTYPE html>
<html lang="en">
<head>
<meta charset="UTF-8">
<title>Velmora Property Inspections – Business Card</title>
<link rel="stylesheet" href="https://fonts.googleapis.com/css2?family=Jost:ital,wght@0,500;0,600;1,500&display=swap">
<style>
  :root {
    --page-bg: #ffffff;
    --card-dark: #151515;
    --card-mid: #2a2a2a;
    --brand-green: #5bba52;
    --soft-white: #e6e7e8;
    --text-white: #ffffff;
  }
  * { margin: 0; padding: 0; box-sizing: border-box; }
  html, body {
    width: 1200px;
    height: 1000px;
    overflow: hidden;
    background: var(--page-bg);
  }
  .canvas {
    position: relative;
    width: 1200px;
    height: 1000px;
  }
  .business-card {
    position: absolute;
    left: 70px;
    top: 217px;
    width: 1048px;
    height: 599px;
    overflow: hidden;
    font-family: "Jost", "Futura", sans-serif;
    color: var(--text-white);
  }
  .card-texture {
    position: absolute;
    inset: 0;
    background: linear-gradient(135deg, var(--card-mid) 0%, var(--card-dark) 55%, #0c0c0c 100%);
  }
  .card-shapes {
    position: absolute;
    inset: 0;
  }
  .contact-block {
    position: absolute;
    left: 38px;
    top: 32px;
  }
  .person-name {
    font-size: 54px;
    font-weight: 600;
    line-height: 1;
    letter-spacing: 0.5px;
  }
  .person-role {
    margin-top: 14px;
    margin-left: 4px;
    font-size: 35px;
    font-style: italic;
    font-weight: 500;
    line-height: 1;
  }
  .company-name {
    margin-top: 12px;
    font-size: 45px;
    font-weight: 500;
    line-height: 1.05;
    letter-spacing: 0.3px;
  }
  .contact-line {
    font-size: 32px;
    font-weight: 600;
    line-height: 1.4;
    letter-spacing: 0.3px;
  }
  .contact-line:first-of-type { margin-top: 8px; }
  .brand-wordmark {
    position: absolute;
    left: 585px;
    top: 474px;
    width: 415px;
    text-align: center;
    font-size: 64px;
    font-weight: 600;
    letter-spacing: 2px;
    color: var(--soft-white);
    line-height: 1;
  }
</style>
</head>
<body>
  <div class="canvas">
    <section class="business-card">
      <div class="card-texture" role="img" aria-label="Dark carbon-fibre weave texture background"></div>
      <svg class="card-shapes" width="1048" height="599" viewBox="0 0 1048 599" aria-hidden="true">
        <polygon class="accent-band" fill="var(--brand-green)"
          points="0,345 628,309 377,599 292,599 405,426 0,441"/>
        <polygon class="accent-wedge" fill="var(--soft-white)"
          points="0,513 285,501 226,599 0,599"/>
      </svg>
      <div class="contact-block">
        <h1 class="person-name">Glen Mirewick</h1>
        <p class="person-role">Home Inspector</p>
        <p class="company-name">Velmora Property Inspections, LLC</p>
        <p class="contact-line">Contact no.: 480-555-0172</p>
        <p class="contact-line">Email: glen@velmora-llc.example</p>
      </div>
      <p class="brand-wordmark">VELMORA</p>
    </section>
  </div>
</body>
</html>
```